Edgy rebranded biz cards KRB

We are rebranding our 20 yr old mortgage company with a new logo and would like cards to compliment our new look.

Target Market(s)

potential home buyers or clients for refinance

Industry/Entity Type

Mortgage Brokerage

Contact Information for Business Card

418 W. Lomita Ave #305
Henderson, NV 89152
702.519.4827 o
702-519-4829 f
www.kestrelridgelending,example
nmls 842019
KRB is an equal housing lender

Font styles to use
Sans Serif

Colors
0455a3
3176b5
0393ce
33a6d7

Requirements
Must have
• space for a photo
Nice to have
• One side with the company info and the other with the person's info

```html
<!DOCTYPE html>
<html lang="en">
<head>
<meta charset="utf-8">
<title>Kestrel Ridge Lending – Business Cards</title>
<link rel="stylesheet" href="https://fonts.googleapis.com/css2?family=Roboto:wght@300;400;700&display=swap">
<style>
  :root {
    --page-bg: #135d96;
    --card-bg: #ffffff;
    --brand-blue: #1273bf;
    --band-blue: #1575bd;
    --rule-grey: #8a8a8a;
    --text-blue: #1a6db5;
    --photo-fill: #dfe8f1;
    --photo-edge: #b9cadb;
  }
  html, body {
    margin: 0;
    padding: 0;
    width: 695px;
    height: 1200px;
    overflow: hidden;
    background: var(--page-bg);
    font-family: "Roboto", Arial, sans-serif;
  }
  .canvas {
    position: relative;
    width: 695px;
    height: 1200px;
  }
  .card {
    position: absolute;
    background: var(--card-bg);
    box-shadow: 0 2px 6px rgba(0,0,0,0.18);
  }
  .card--person { left: 137px; top: 618px; width: 417px; height: 236px; }
  .card--company { left: 133px; top: 892px; width: 416px; height: 235px; }

  .photo-space {
    position: absolute;
    left: 36px; top: 18px;
    width: 78px; height: 100px;
    background: linear-gradient(180deg, var(--photo-fill), #cfdbe8);
    border: 1px solid var(--photo-edge);
    box-sizing: border-box;
  }

  .brand-name {
    position: absolute;
    margin: 0;
    color: var(--brand-blue);
    font-weight: 700;
    text-transform: uppercase;
    text-align: center;
    line-height: 1.05;
    letter-spacing: 0.5px;
  }
  .card--person .brand-name {
    left: 216px; top: 36px; width: 180px;
    font-size: 22px;
  }
  .card--company .brand-name {
    left: 0; top: 62px; width: 416px;
    font-size: 30px;
  }

  .holder-name {
    position: absolute;
    left: 36px; top: 135px;
    margin: 0;
    font-size: 21px;
    font-weight: 400;
    letter-spacing: 1px;
    color: var(--text-blue);
  }
  .name-rule {
    position: absolute;
    left: 36px; top: 168px;
    width: 367px; height: 3px;
    background: var(--rule-grey);
  }
  .contact {
    position: absolute;
    display: flex;
    align-items: center;
    gap: 8px;
    color: var(--text-blue);
    letter-spacing: 0.3px;
    white-space: nowrap;
  }
  .contact svg { flex: none; }
  .contact--web   { left: 36px; top: 180px; font-size: 9.5px; }
  .contact--fax   { left: 36px; top: 203px; font-size: 11px; letter-spacing: 0.6px; }
  .contact--phone { left: 250px; top: 178px; font-size: 13.5px; letter-spacing: 0.6px; }
  .contact--addr  { left: 250px; top: 205px; font-size: 8.5px; line-height: 1.3; }

  .compliance {
    position: absolute;
    left: 0; top: 160px;
    width: 100%;
    margin: 0;
    text-align: center;
    font-size: 10px;
    letter-spacing: 0.8px;
    color: var(--rule-grey);
  }

  .web-band {
    position: absolute;
    left: 0; bottom: 0;
    width: 100%; height: 28px;
    background: var(--band-blue);
    color: #ffffff;
    font-size: 14px;
    letter-spacing: 1.4px;
    display: flex;
    align-items: center;
    justify-content: center;
  }
</style>
</head>
<body>
<main class="canvas">

  <section class="card card--person" aria-label="Business card, person side">
    <div class="photo-space" role="img" aria-label="Space for the loan officer's portrait photo"></div>

    <p class="brand-name">Kestrel Ridge<br>Lending</p>

    <h1 class="holder-name">Your name</h1>
    <div class="name-rule"></div>

    <div class="contact contact--web">
      <svg width="15" height="15" viewBox="0 0 16 16" aria-hidden="true">
        <rect x="1" y="1" width="14" height="14" rx="2" fill="none" stroke="#1a6db5" stroke-width="1.5"/>
        <circle cx="8" cy="8" r="4" fill="none" stroke="#1a6db5" stroke-width="1.2"/>
        <path d="M4 8h8M8 4v8" stroke="#1a6db5" stroke-width="1"/>
      </svg>
      <span>www.kestrelridgelending.example</span>
    </div>

    <div class="contact contact--fax">
      <svg width="15" height="15" viewBox="0 0 16 16" aria-hidden="true">
        <rect x="1" y="1" width="14" height="14" rx="2" fill="none" stroke="#1a6db5" stroke-width="1.5"/>
        <path d="M5 4c-1 1-1 4 1.5 6.5S11 13 12 12l-1.5-1.8-1.3.8C8 10.5 6 8.5 5.6 7.3l.8-1.3z" fill="#1a6db5"/>
      </svg>
      <span>702-519-4829 f</span>
    </div>

    <div class="contact contact--phone">
      <svg width="18" height="20" viewBox="0 0 18 20" aria-hidden="true">
        <rect x="1" y="4" width="16" height="15" rx="2" fill="none" stroke="#1a6db5" stroke-width="1.6"/>
        <rect x="6" y="1" width="6" height="3" fill="#1a6db5"/>
        <rect x="4" y="9" width="10" height="6" rx="1" fill="#1a6db5"/>
      </svg>
      <span>702.519.4827 o</span>
    </div>

    <div class="contact contact--addr">
      <svg width="18" height="18" viewBox="0 0 18 18" aria-hidden="true">
        <rect x="1" y="1" width="16" height="16" rx="2" fill="none" stroke="#1a6db5" stroke-width="1.6"/>
        <path d="M9 4a3.2 3.2 0 0 0-3.2 3.2C5.8 10 9 14 9 14s3.2-4 3.2-6.8A3.2 3.2 0 0 0 9 4z" fill="#1a6db5"/>
        <circle cx="9" cy="7.3" r="1.2" fill="#ffffff"/>
      </svg>
      <span>418 W. Lomita Ave #305<br>Henderson, NV 89152</span>
    </div>
  </section>

  <section class="card card--company" aria-label="Business card, company side">
    <p class="brand-name">Kestrel Ridge<br>Lending</p>
    <p class="compliance">NMLS 842019 · KRB is an equal housing lender</p>
    <div class="web-band">www.kestrelridgelending.example</div>
  </section>

</main>
</body>
</html>
```